Childrens Business Card Design Project

We have an existing logo attached which we'd like to use as part of our new business card design.

The design needs to be relatively gender neutral and contain bright colours.

In terms of look and feel think:

Fun, Modern, Quality (as opposed to cheap!) and of course Party!

Single or double sided - i am not decided on either one yet - ideally i'd like to see designs for both because if you think stylistically it would benefit having two sides then please try it out!

I think the challenge here is finding a really good background colour (if you think it needs one) and also choosing an eye grabbing text that compliments the existing logo - do that an you are onto a winner! I have another image for the business (which i have attached) which uses stripes so i am keen to see a design that incorporates this to tie in all my collateral.

The copy required is as follows (not necesarily in this order)

Bookings/Enquiries:

Tilda

T: 0498 217 503
E: enquiries@brightfoxparties.example.au

ABN: 47 302 658 114

Any feedback on text is welcomed - please message me or add to the discussion.

Reason: Hi All, I have received some promising designs, but overall i am not impressed with the quality of the work so have extended the deadline as this project has been committed. I will aim to attach some business card examples to the brief tomorrow to give further guidance as a whole but please do not submit any designs on a generic background that are not related to the theme, have been carelessly placed with overlapping elements - it just looks sloppy. For those who have read the brief an incorporated stripes or even spots this is on target as it convey's a party theme, however please work on getting the colours for the contact details by either a bold solid strip to highlight or some other way to frame it. When it comes to the logo, some people have removed the characters all together and changed the colour of the wording - this is fine. Also feel free to balloons starts - but keep it classy and watch your placement of these. I hope this helps and for the designs i would like to see revisions for i will aim to get back to you individually over the next day or so. Many thanks all.

Target Market(s)

Mothers in the suburbs of Australia with a disposal able income, children aged between 1-7 years old.

Industry/Entity Type

Business

Requirements
Must have
• The font and wording positioning must compliment the logo.

```html
<!DOCTYPE html>
<html lang="en">
<head>
<meta charset="utf-8">
<title>Bright Fox – Business Card</title>
<link rel="stylesheet" href="https://fonts.googleapis.com/css2?family=Exo+2:wght@400;600&display=swap">
<style>
  :root {
    --backdrop: #d7d7d7;
    --card-blue: #00b0ea;
    --deep-blue: #0a98cf;
    --bubble: rgba(255, 255, 255, 0.28);
    --bubble-soft: rgba(255, 255, 255, 0.18);
    --white: #ffffff;
    --rim: #e4e4e4;
    --brand-red: #e2352d;
  }
  html, body {
    margin: 0;
    padding: 0;
    width: 1200px;
    height: 1000px;
    overflow: hidden;
    background: var(--backdrop);
  }
  .canvas {
    position: relative;
    width: 1200px;
    height: 1000px;
  }
  .business-card {
    position: absolute;
    left: 181px;
    top: 246px;
    width: 838px;
    height: 507px;
    overflow: hidden;
    font-family: "Exo 2", sans-serif;
    color: var(--white);
  }
  .card-art {
    position: absolute;
    inset: 0;
  }
  .brand-name {
    position: absolute;
    left: 40px;
    top: 100px;
    width: 330px;
    text-align: center;
    font-size: 46px;
    font-weight: 600;
    color: var(--brand-red);
    letter-spacing: 1px;
  }
  .contact-block {
    position: absolute;
    left: 434px;
    top: 246px;
    text-shadow: 0 1px 2px rgba(0, 0, 0, 0.15);
  }
  .contact-name {
    margin: 0;
    font-size: 30px;
    font-weight: 600;
    line-height: 36px;
  }
  .contact-role {
    margin: 0;
    font-size: 27px;
    font-weight: 400;
    line-height: 34px;
  }
  .contact-details {
    position: absolute;
    left: 434px;
    top: 382px;
    width: 390px;
    font-size: 20px;
    letter-spacing: -0.2px;
    line-height: 36px;
    text-shadow: 0 1px 2px rgba(0, 0, 0, 0.15);
  }
  .contact-details p { margin: 0; white-space: nowrap; }
</style>
</head>
<body>
<main class="canvas">
  <section class="business-card">
    <svg class="card-art" width="838" height="507" viewBox="0 0 838 507" aria-hidden="true">
      <rect width="838" height="507" fill="var(--card-blue)"/>
      <circle cx="820" cy="80" r="82" fill="var(--bubble)"/>
      <circle cx="621" cy="207" r="60" fill="var(--bubble)"/>
      <circle cx="350" cy="302" r="46" fill="var(--bubble)"/>
      <circle cx="24" cy="376" r="64" fill="var(--bubble)"/>
      <circle cx="480" cy="58" r="12" fill="var(--bubble)"/>
      <circle cx="283" cy="436" r="13" fill="var(--bubble)"/>
      <circle cx="821" cy="266" r="12" fill="var(--bubble)"/>
      <circle cx="649" cy="379" r="8" fill="var(--bubble-soft)"/>
      <circle cx="486" cy="512" r="32" fill="var(--bubble)"/>
      <circle cx="858" cy="460" r="40" fill="var(--bubble)"/>
      <path d="M520 0 Q530 60 510 110" stroke="var(--bubble)" stroke-width="2" fill="none"/>
      <path d="M740 40 Q720 80 740 110" stroke="var(--bubble)" stroke-width="2" fill="none"/>
      <path d="M600 140 Q650 145 680 175" stroke="var(--bubble)" stroke-width="2" fill="none"/>
      <path d="M20 460 Q90 420 120 390" stroke="var(--bubble)" stroke-width="2" fill="none"/>
      <line x1="416" y1="326" x2="416" y2="496" stroke="var(--bubble)" stroke-width="1.5"/>
      <line x1="416" y1="496" x2="830" y2="496" stroke="var(--bubble)" stroke-width="1.5"/>
      <line x1="480" y1="327" x2="660" y2="327" stroke="var(--bubble)" stroke-width="2"/>
      <line x1="20" y1="487" x2="400" y2="487" stroke="var(--bubble)" stroke-width="2"/>
      <circle cx="224" cy="96" r="238" fill="var(--deep-blue)"/>
      <circle cx="218" cy="86" r="232" fill="var(--rim)"/>
      <circle cx="214" cy="82" r="228" fill="var(--white)"/>
    </svg>
    <div class="brand-name">Bright Fox</div>
    <div class="contact-block">
      <p class="contact-name">Tilda</p>
      <p class="contact-role">Bookings/Enquiries</p>
    </div>
    <div class="contact-details">
      <p>ABN: 47 302 658 114</p>
      <p>T: 0498 217 503</p>
      <p>E: enquiries@brightfoxparties.example.au</p>
    </div>
  </section>
</main>
</body>
</html>
```